Letterhead for 3 attorney Workers' Comp law firm

We are a 3 attorney law office. We specialize in Workers' Compensation. Our office represents workers who are injured on the job, and the estates of workers who are killed one the job.
When we started our office, we created our own letterhead & have been using it for years. We've just recently hired the 3rd attorney, and were going to just add his name to the letterhead, but have decided we wanted to get a professionally designed letterhead and business cards at this point.
We want something that looks clean and professional. It must look good in black and white because we often make multiple copies of our documents. We're hoping for a design that resonates confidence, reliability and experience.
The design must include the firm name: Thornbury & Calder, PLLC. We would like the PLLC to be small compared to the Thornbury & Calder graphic. We also want to incorporate the attorney names: Ivar Thornbury, Delia Calder, and Glen Rutledge. Our current letterhead has our contact info in the footer at the bottom of the page. We like that design, but are open to the idea of having it at the top. We'll leave that at the discretion of the designer. Our contact info is as follows: 482 S. Harrow Avenue, Suite 310 Bellingham, WA 98417 Phone: 360-555-2917, Fax: 360-555-4068, and our website: www.thornburycalder.example
Target Market(s)
Clients, courts, other legal offices, doctors offices. These are the people who see our letterhead most frequently. It's not so much for marketing purposes, mainly so that we have a professional image when sending out documents.
Industry/Entity Type
Law Firm
Contact Information for Business Card
On the back of the business card: it can be designed, or be a template for filling in appointment reminder information (i.e. date, time, etc)
Colors
Designer to choose colors to be used in the design.
Requirements
Must have
- Must have our firm name at the top.
- Must include the attorney names.
- Must have all of our contact information (can be at top or bottom - whatever looks best with the design)
Nice to have
- A strong, confident design
Should not have
- We don't want the design to be playful, cartoony or busy.

```html
<!DOCTYPE html>
<html lang="en">
<head>
<meta charset="utf-8">
<title>Thornbury &amp; Calder, PLLC — Letterhead</title>
<link href="https://fonts.googleapis.com/css2?family=Lexend+Exa:wght@300&family=Open+Sans:ital,wght@0,400;1,400&display=swap" rel="stylesheet">
<style>
  :root {
    --backdrop: #8cc2e2;
    --paper: #ffffff;
    --paper-tint: #eef5fc;
    --brand-blue: #1ea3dc;
    --accent-grey: #c9c9c9;
    --text-grey: #8a8a8a;
    --body-grey: #555a60;
    --watermark: #e3e5ea;
  }
  * { margin: 0; padding: 0; box-sizing: border-box; }
  html, body { width: 1200px; height: 784px; overflow: hidden; }
  body {
    background: var(--backdrop);
    display: flex;
    align-items: center;
    justify-content: center;
    font-family: "Open Sans", Arial, sans-serif;
  }
  .letterhead {
    position: relative;
    width: 572px;
    height: 740px;
    background: radial-gradient(ellipse at 30% 20%, var(--paper) 55%, var(--paper-tint) 100%);
    overflow: hidden;
  }
  .corner-accent { position: absolute; top: 0; height: 6px; display: flex; }
  .corner-accent span { display: block; height: 100%; }
  .corner-accent--left { left: 0; }
  .corner-accent--right { right: 0; }
  .accent-grey { background: var(--accent-grey); }
  .accent-blue { background: var(--brand-blue); }

  .firm-header { position: absolute; top: 22px; left: 26px; }
  .firm-name {
    font-family: "Lexend Exa", "Helvetica Neue", sans-serif;
    font-weight: 300;
    font-size: 19px;
    color: var(--brand-blue);
    letter-spacing: -0.5px;
    white-space: nowrap;
  }
  .firm-name .entity { font-size: 9px; letter-spacing: 0; }
  .attorney-list {
    margin-top: 3px;
    font-style: italic;
    font-size: 8.5px;
    color: var(--text-grey);
    white-space: nowrap;
  }

  .contact-block {
    position: absolute;
    top: 270px;
    right: 22px;
    font-size: 8px;
    line-height: 1.45;
    color: var(--body-grey);
    list-style: none;
  }
  .contact-block li { display: flex; align-items: flex-start; gap: 4px; white-space: nowrap; }
  .contact-block svg { flex: none; width: 8px; height: 8px; margin-top: 2px; }
  .contact-block .indent { padding-left: 12px; }

  .watermark {
    position: absolute;
    left: 18px;
    bottom: 14px;
    font-family: "Lexend Exa", "Helvetica Neue", sans-serif;
    font-weight: 300;
    font-size: 38px;
    letter-spacing: -2px;
    color: var(--watermark);
    white-space: nowrap;
  }
  .watermark .entity { font-size: 20px; letter-spacing: 0; }

  .footer-band { position: absolute; left: 0; bottom: 0; width: 100%; height: 7px; display: flex; }
  .footer-band .accent-blue { width: 70%; }
  .footer-band .accent-grey { width: 30%; }
</style>
</head>
<body>
  <main class="letterhead">
    <div class="corner-accent corner-accent--left">
      <span class="accent-grey" style="width:26px"></span>
      <span class="accent-blue" style="width:22px"></span>
    </div>
    <div class="corner-accent corner-accent--right">
      <span class="accent-grey" style="width:26px"></span>
      <span class="accent-blue" style="width:46px"></span>
    </div>

    <header class="firm-header">
      <h1 class="firm-name">Thornbury &amp; Calder <span class="entity">PLLC</span></h1>
      <p class="attorney-list">Ivar Thornbury | Delia Calder | Glen Rutledge</p>
    </header>

    <ul class="contact-block">
      <li>
        <svg viewBox="0 0 10 10"><circle cx="5" cy="5" r="5" fill="#1ea3dc"/><path d="M5 2a2 2 0 0 0-2 2c0 1.5 2 4 2 4s2-2.5 2-4a2 2 0 0 0-2-2z" fill="#fff"/></svg>
        <span>482 S. Harrow Avenue, Suite 310</span>
      </li>
      <li class="indent">Bellingham, WA 98417</li>
      <li>
        <svg viewBox="0 0 10 10"><circle cx="5" cy="5" r="5" fill="#1ea3dc"/><path d="M3 2.5l1.2 0 .6 1.5-.8.6a4 4 0 0 0 1.4 1.4l.6-.8 1.5.6 0 1.2c-2.8.2-4.7-1.7-4.5-4.5z" fill="#fff"/></svg>
        <span>360-555-2917</span>
        <svg viewBox="0 0 10 10"><circle cx="5" cy="5" r="5" fill="#1ea3dc"/><rect x="2.5" y="4" width="5" height="3" fill="#fff"/><rect x="3.5" y="2.5" width="3" height="1.5" fill="#fff"/></svg>
        <span>360-555-4068</span>
      </li>
      <li>
        <svg viewBox="0 0 10 10"><circle cx="5" cy="5" r="5" fill="#1ea3dc"/><circle cx="5" cy="5" r="2.6" fill="none" stroke="#fff" stroke-width=".8"/><path d="M2.4 5h5.2M5 2.4v5.2" stroke="#fff" stroke-width=".6"/></svg>
        <span>www.thornburycalder.example</span>
      </li>
    </ul>

    <p class="watermark" aria-hidden="true">Thornbury &amp; Calder <span class="entity">PLLC</span></p>

    <div class="footer-band">
      <span class="accent-blue"></span>
      <span class="accent-grey"></span>
    </div>
  </main>
</body>
</html>
```